Australian Online Training Organisation needs a Website Design

We need a Web Design ideally using a Wordpress Divi template which will represent an Australian Online Training Company.

(Pendlow Online Training)

The website will represent a range of short courses with an emphasis on business, brightnet, leadership etc.

The website will 'shell out' to the third party portal where 'bookings' occur. I am imaging a fantastic looking web design with perhaps 5-6 pages.

I am wondering if a selection of courses including the below list can be incorporated?

The variety of courses include :

Workplace Safety
Sales Training
Leadership
Process Management
Problem Solving
Project Management
Business Planning
Meetings and Events
Emotional Intelligence
Human Resources
Administrative Essentials
Customer Service
Career Development
Conflict Resolution
Train the Trainer
Supervisors and Managers
Internet marketing
Communications
Team Building
Marketing
Finance
Writing
Job Search Skills
Public Speaking
Negotiation Skills
Talent Management
Brightnet Deskline 2016
BDS Preparation for Deskline 2010
Deskline 2013
Deskline 2010
Upgrading to Deskline 2010
Computer Fundamentals
Upgrading to Deskline 2007
Deskline 2003
Deskline 2002
Varlo Deskline X3
Core Essentials
Deskline 2007

Thank you so much for all of the amazing designs we received. We were so happy with so many elements that it was very hard to choose. Our top two were very hard to decide upon but we look forward to working more with both of these talents into the future. Thank you again.

Target Market(s)

Professionals, students and workers who would like to improve their skills with online training in over 500 + courses -

Industry/Entity Type

It Company

Number of Pages Required

5+ page

Font styles to use
Sans Serif

Colors
3276b5
faa54b
0355a3
fac994

Requirements
Must have
• Ideally would use Wordpress theme (Divi for example or other)
• Very smart front end
• Will upload logo soon
• (Pendlow Online Training)
• pendlowonlinetraining.edu.au
• Graphics of 'people' pretty important - with a variety of ages.
Nice to have
• Interesting page
• National presence
• A bit University looking
• Professional
• Graphics of people
• Blog
• Graphics of people
• Age range from job seekers, to business folk, etc

```html
<!DOCTYPE html>
<html lang="en">
<head>
<meta charset="utf-8">
<title>Pendlow Online Training</title>
<link rel="stylesheet" href="https://fonts.googleapis.com/css2?family=Questrial&family=Roboto:wght@400;500;700&family=Josefin+Sans:wght@600;700&display=swap">
<style>
:root{
  --bar:#454850;
  --orange:#f5a04a;
  --orange-soft:#fac994;
  --blue:#3276b5;
  --navy:#1f3a5f;
  --ink:#222;
  --muted:#777;
  --band:#f6f4f4;
  --strip:#f1f1f1;
  --white:#fff;
}
*{box-sizing:border-box;margin:0;padding:0}
html,body{width:1200px;height:2250px;overflow:hidden;background:var(--white)}
body{position:relative;font-family:"Questrial",sans-serif;color:var(--ink)}
.abs{position:absolute}
svg{display:inline-block;vertical-align:middle}

.topbar{left:0;top:0;width:1200px;height:53px;background:var(--bar);color:var(--white);font-family:"Roboto",sans-serif;font-size:16px}
.topbar .contact{left:38px;top:15px;display:flex;gap:36px}
.topbar .contact span{display:flex;align-items:center;gap:8px}
.topbar .social{right:72px;top:15px;display:flex;gap:16px}

.header{left:0;top:53px;width:1200px;height:153px;background:var(--white);border-bottom:1px solid #ddd}
.brand{left:64px;top:20px;width:130px;text-align:center;color:var(--navy);font-size:28px;line-height:1.05;letter-spacing:1px}
.brand .mark{display:block;width:40px;height:40px;margin:0 auto 12px;background:var(--navy)}
.brand small{display:block;font-size:11px;letter-spacing:1px;margin-top:4px;color:var(--orange)}
.nav{left:452px;top:72px;display:flex;gap:31px;font-family:"Roboto",sans-serif;font-weight:500;font-size:19px;color:#333}
.search{left:1053px;top:71px;width:25px;height:24px;border:2px solid #333;display:flex;align-items:center;justify-content:center}

.hero{left:0;top:207px;width:1200px;height:540px;background:linear-gradient(120deg,#3b3d40 0%,#55595d 30%,#6f6a63 52%,#4a4e52 70%,#8b9095 100%)}
.hero h1{position:absolute;left:0;top:200px;width:1200px;text-align:center;font-family:"Josefin Sans",sans-serif;font-weight:700;font-size:42px;line-height:48px;letter-spacing:-1.2px;color:var(--white)}
.hero .cta{position:absolute;left:492px;top:344px;width:207px;height:58px;border:2px solid var(--white);border-radius:6px;color:var(--white);font-family:"Roboto",sans-serif;font-size:24px;display:flex;align-items:center;justify-content:center}

.welcome{left:0;top:747px;width:1200px;height:233px;background:var(--band);text-align:center}
.welcome h2{position:absolute;left:0;top:30px;width:1200px;font-weight:400;font-size:28px;color:var(--ink)}
.welcome h2 em{font-style:normal;color:var(--orange)}
.welcome .rule{position:absolute;left:533px;top:66px}
.welcome p{position:absolute;left:60px;top:111px;width:1080px;font-size:17.5px;line-height:22px;color:#222}

.feature{top:996px;width:300px}
.feature h3{position:absolute;left:54px;top:2px;font-family:"Josefin Sans",sans-serif;font-weight:700;font-size:21px;color:var(--orange)}
.feature p{position:absolute;left:54px;top:30px;width:235px;font-size:14px;line-height:17px;color:#333}
.feature svg{position:absolute;left:0;top:0}

.courses-head{left:0;top:1178px;width:1200px;text-align:center}
.courses-head h2{font-family:"Roboto",sans-serif;font-weight:500;font-size:21px;color:var(--orange)}
.courses-head p{font-size:10px;color:#444;margin-top:3px}
.arrows{left:1093px;top:1177px;display:flex;gap:8px}

.card{top:1245px;width:275px}
.card .photo{width:260px;height:135px}
.card h4{position:absolute;left:-2px;top:153px;font-family:"Roboto",sans-serif;font-weight:400;font-size:17px;color:#222}
.card .price{position:absolute;left:205px;top:166px;text-align:center;font-family:"Roboto",sans-serif;color:var(--orange);font-size:21px;line-height:20px}
.card .price small{display:block;font-size:10px;color:#222;font-weight:500}
.card .stars{position:absolute;left:-6px;top:184px}
.card .reviews{position:absolute;left:-2px;top:203px;font-size:10px;color:#555}
.card .divider{position:absolute;left:-6px;top:236px;width:275px;height:1px;background:#ddd}
.card .tutor{position:absolute;left:-6px;top:245px;display:flex;gap:14px;align-items:center}
.card .avatar{width:30px;height:30px;border-radius:50%;background:#c79a86}
.card .tutor b{display:block;font-family:"Roboto",sans-serif;font-size:11px;color:#222}
.card .tutor span{font-size:10px;color:var(--muted)}

.testimonial-photo{left:150px;top:1560px;width:340px;height:300px;border-radius:6px;background:linear-gradient(180deg,#e9eef3 0%,#bcd0e4 35%,#9cb8d6 70%,#ffffff 100%)}
.testimonial{left:542px;top:1603px;width:560px}
.testimonial h3{font-family:"Roboto",sans-serif;font-weight:700;font-size:24px;color:var(--orange)}
.testimonial h4{margin-top:22px;font-weight:400;font-size:20px;line-height:24px;color:#111}
.testimonial p{margin-top:24px;font-size:13px;line-height:16px;color:#222}

.partners{left:0;top:1923px;width:1200px;height:129px;background:var(--strip);display:flex;align-items:center;justify-content:space-around;padding:0 20px;font-family:"Roboto",sans-serif;font-weight:500;font-size:30px;color:#6e6e6e}
.partners span{display:flex;align-items:center;gap:8px}
.partners i{display:block;width:16px;height:16px;background:#8a8a8a}

.footer{left:0;top:2052px;width:1200px;height:198px;background:var(--bar);color:var(--white)}
.footer h5{font-family:"Roboto",sans-serif;font-weight:700;font-size:17px}
.footer .col{position:absolute;top:20px}
.footer .col p{font-family:"Roboto",sans-serif;font-weight:500;font-size:13px;line-height:17px;margin-top:18px}
.footer .field{margin-top:22px;width:172px;height:18px;border:1px solid #888;border-radius:5px;font-size:11px;color:#bbb;padding:1px 10px}
.footer .line{display:flex;gap:10px;align-items:flex-start;font-family:"Roboto",sans-serif;font-size:13px;margin-top:14px}
.footer .line small{font-size:10.5px;line-height:13px}
.map{left:924px;top:2064px;width:138px;height:114px;background:linear-gradient(160deg,#d7d9da,#b8bcbf);border:1px solid #999}
.footer .address{position:absolute;left:918px;top:146px;width:250px;font-family:"Roboto",sans-serif;font-weight:700;font-size:10px;line-height:13px}
</style>
</head>
<body>

<div class="abs topbar">
  <div class="abs contact">
    <span><svg width="16" height="12" viewBox="0 0 16 12"><rect x="1" y="1" width="14" height="10" fill="none" stroke="#fff" stroke-width="1.5"/><path d="M1 1l7 6 7-6" fill="none" stroke="#fff" stroke-width="1.5"/></svg>hello@pendlowonline.edu.au</span>
    <span><svg width="14" height="14" viewBox="0 0 14 14"><path d="M3 1l3 3-2 2c1 2 2 3 4 4l2-2 3 3-2 2C6 13 1 8 1 3z" fill="#fff"/></svg>1800 555 014</span>
  </div>
  <div class="abs social"><span>Friendly</span><span>Chirp</span><span>Pixgram</span></div>
</div>

<div class="abs header">
  <div class="abs brand"><span class="mark"></span>PENDLOW<small>ONLINE TRAINING</small></div>
  <nav class="abs nav"><span>Home</span><span>Courses</span><span>Blog</span><span>Employees</span><span>Contact Us</span><span>About Us</span></nav>
  <div class="abs search"><svg width="13" height="13" viewBox="0 0 13 13"><circle cx="5.5" cy="5.5" r="3.8" fill="none" stroke="#333" stroke-width="1.8"/><path d="M8.5 8.5l3.5 3.5" stroke="#333" stroke-width="1.8"/></svg></div>
</div>

<section class="abs hero" role="img" aria-label="Photo of students working at computers in a training room with an instructor">
  <h1>SPECIALISE IN ONLINE BRIGHTNET<br>PRODUCT TRAINING</h1>
  <div class="cta">Admission Now</div>
</section>

<section class="abs welcome">
  <h2>WELCOME <em>TO PENDLOW</em></h2>
  <svg class="rule" width="134" height="30" viewBox="0 0 134 30"><path d="M0 15h50M84 15h50" stroke="#999" stroke-width="1"/><path d="M58 3h18v24l-9-7-9 7z" fill="none" stroke="#f5a04a" stroke-width="2.5"/></svg>
  <p>Pendlow Online Training is one of Australia's leading provider of flexible and affordable online continuing professional<br>development programs, with over 600 online courses now available.Our range of self- paced online courses<br>are delivered completely online via our e-learning system 24/7.We offer a range of popular online courses in accounting,<br>finance, bookkeeping, management, marketing, information technology, project management and more.</p>
</section>

<div class="abs feature" style="left:75px">
  <svg width="36" height="30" viewBox="0 0 36 30"><path d="M2 7h8c6 0 10 16 16 16h6M2 23h8c6 0 10-16 16-16h6" fill="none" stroke="#f5a04a" stroke-width="4"/><path d="M28 1l7 6-7 6zM28 17l7 6-7 6z" fill="#f5a04a"/></svg>
  <h3>FEXIBILE</h3>
  <p>Pendlow provide an online learning platformwhich fits into your lifestyle and work commitments.&nbsp; You study anywhere, anytime!</p>
</div>
<div class="abs feature" style="left:444px">
  <svg width="38" height="32" viewBox="0 0 38 32"><path d="M8 2h22l7 9-18 19L1 11z M1 11h36 M13 2l-4 9 10 19 10-19-4-9" fill="none" stroke="#f5a04a" stroke-width="2"/></svg>
  <h3 style="left:46px">VALUE</h3>
  <p style="left:46px;width:260px">Our innovative online training approach allows us to deliver exceptional training in over 600 industry</p>
</div>
<div class="abs feature" style="left:856px">
  <svg width="34" height="38" viewBox="0 0 34 38"><circle cx="17" cy="9" r="8" fill="#f5a04a"/><path d="M3 30c0-8 6-12 14-12s14 4 14 12z" fill="#f5a04a"/><rect x="0" y="31" width="34" height="6" fill="#f5a04a"/></svg>
  <h3 style="left:46px">EXPERIENCE</h3>
  <p style="left:46px;width:250px">Pendlow is one of Australia's largest and leading providers of training services in nationally.</p>
</div>

<div class="abs courses-head">
  <h2>Courses from renowned Instructors</h2>
  <p>Best courses from best instructors on the worlds favorite site</p>
</div>
<div class="abs arrows">
  <svg width="27" height="27" viewBox="0 0 27 27"><circle cx="13.5" cy="13.5" r="12" fill="none" stroke="#f5a04a" stroke-width="2"/><path d="M16 8l-6 5.5 6 5.5" fill="none" stroke="#f5a04a" stroke-width="2.5"/></svg>
  <svg width="27" height="27" viewBox="0 0 27 27"><circle cx="13.5" cy="13.5" r="12" fill="none" stroke="#f5a04a" stroke-width="2"/><path d="M11 8l6 5.5-6 5.5" fill="none" stroke="#f5a04a" stroke-width="2.5"/></svg>
</div>

<article class="abs card" style="left:112px">
  <div class="photo" role="img" aria-label="Photo of a sales team meeting around a boardroom table" style="background:linear-gradient(180deg,#e8ecef 0%,#c9d0d6 45%,#5a5f66 75%,#2c2f33 100%)"></div>
  <h4>Sales Trainings</h4>
  <div class="price">$19<small>PER MONTH</small></div>
  <svg class="stars" width="100" height="16" viewBox="0 0 100 16"><defs><path id="star" d="M8 1l2 5h5l-4 3 1.6 5L8 11 3.4 14 5 9 1 6h5z"/></defs><g fill="none" stroke-width="1.2"><use href="#star" stroke="#f5a04a"/><use href="#star" x="19" stroke="#f5a04a"/><use href="#star" x="38" stroke="#f5a04a"/><use href="#star" x="57" stroke="#bbb"/><use href="#star" x="76" stroke="#bbb"/></g></svg>
  <div class="reviews">(10 Reviews)</div>
  <div class="divider"></div>
  <div class="tutor"><div class="avatar"></div><div><b>CORALIE VANTNER</b><span>Training Officer</span></div></div>
</article>
<article class="abs card" style="left:489px">
  <div class="photo" role="img" aria-label="Photo of a leader presenting to colleagues at a table" style="background:linear-gradient(180deg,#f1f4f7 0%,#d6e1ec 40%,#6f8fb3 70%,#eef1f4 100%)"></div>
  <h4>Leadership</h4>
  <div class="price">$19<small>PER MONTH</small></div>
  <svg class="stars" width="100" height="16" viewBox="0 0 100 16"><g fill="none" stroke-width="1.2"><use href="#star" stroke="#f5a04a"/><use href="#star" x="19" stroke="#f5a04a"/><use href="#star" x="38" stroke="#f5a04a"/><use href="#star" x="57" stroke="#bbb"/><use href="#star" x="76" stroke="#bbb"/></g></svg>
  <div class="reviews">(10 Reviews)</div>
  <div class="divider"></div>
  <div class="tutor"><div class="avatar"></div><div><b>CORALIE VANTNER</b><span>Training Officer</span></div></div>
</article>
<article class="abs card" style="left:850px">
  <div class="photo" role="img" aria-label="Photo of a worker in a safety vest holding an orange hard hat on a site" style="background:linear-gradient(100deg,#7b7872 0%,#a9a59c 35%,#e26a22 60%,#d9531c 80%,#3a3a3a 100%)"></div>
  <h4 style="top:156px">Workplace Safety</h4>
  <div class="price" style="top:169px">$19<small>PER MONTH</small></div>
  <svg class="stars" style="top:187px" width="100" height="16" viewBox="0 0 100 16"><g fill="none" stroke-width="1.2"><use href="#star" stroke="#f5a04a"/><use href="#star" x="19" stroke="#f5a04a"/><use href="#star" x="38" stroke="#f5a04a"/><use href="#star" x="57" stroke="#bbb"/><use href="#star" x="76" stroke="#bbb"/></g></svg>
  <div class="reviews" style="top:206px">(10 Reviews)</div>
  <div class="divider"></div>
  <div class="tutor"><div class="avatar"></div><div><b>CORALIE VANTNER</b><span>Training Officer</span></div></div>
</article>

<div class="abs testimonial-photo" role="img" aria-label="Photo of a smiling man in a light blue shirt with arms spread wide"></div>
<section class="abs testimonial">
  <h3>CORALIE VANTNER</h3>
  <h4>TeamRise Education<br>&nbsp;Training Solutions</h4>
  <p>"The package I purchased will allow me to grow my practice.<br>&nbsp;The product you offer is amazing"</p>
</section>

<section class="abs partners">
  <span>Steadymail</span>
  <span>rivermart</span>
  <span>ParcelGo</span>
  <span><i></i>Brightnet</span>
  <span>Shorely</span>
  <span style="font-size:14px;letter-spacing:3px">HALBROOK AERO</span>
</section>

<footer class="abs footer">
  <div class="col" style="left:100px;width:210px">
    <h5>Newsletter</h5>
    <p>Lorem ipsum dolor sit amet,<br>feugiat delicata liberavisse id cum,</p>
    <div class="field">Email address*</div>
  </div>
  <div class="col" style="left:335px;width:245px">
    <h5>Contact Info :</h5>
    <div class="line"><svg width="12" height="16" viewBox="0 0 12 16"><path d="M6 0a6 6 0 0 0-6 6c0 4 6 10 6 10s6-6 6-10a6 6 0 0 0-6-6z" fill="#e0463c"/><circle cx="6" cy="6" r="2" fill="#fff"/></svg><small>ABN 51902447118&nbsp; Head Office, 48 Marrick Lane, Innovation Park,</small></div>
    <div class="line"><svg width="13" height="13" viewBox="0 0 14 14"><rect width="14" height="14" rx="3" fill="#3cae9a"/><path d="M4 3l2 2-1 1c.6 1.2 1.5 2 2.6 2.6l1-1 2 2-1.4 1.4C6 10.5 3.5 8 2.6 4.4z" fill="#fff"/></svg>1800 555 014</div>
    <div class="line"><svg width="14" height="12" viewBox="0 0 14 12"><rect x="0" y="2" width="14" height="10" fill="#3cae9a"/><path d="M0 2l7 5 7-5" fill="none" stroke="#fff" stroke-width="1.2"/></svg>enquiries@pendlowonline.edu.au</div>
  </div>
  <div class="col" style="left:601px;width:270px">
    <h5>Company History</h5>
    <p>Lorem ipsum dolor sit amet,<br>feugiat delicata liberavisse id cum,<br>no quo maiorum intellegebat, liber<br>regione eu sit. Mea cu case ludus integre,<br>vide viderer eleifend ex mea</p>
  </div>
  <div class="address">ABN 51902447118&nbsp; Head Office,<br>48 Marrick Lane, Innovation Park,<br>Carlow 6190 PO Box 3310 Carlow DC 6190</div>
</footer>
<div class="abs map" role="img" aria-label="Street map showing the head office location"></div>

</body>
</html>
```